Korimo Business Cards

Korimo is a software startup and we are looking for business cards that help convey our employee personalities, as well as the professionalism of the company.
Our company font is Comfortaa - and the company logo is attached (we are okay having the text beside the logo if applicable) where we can find the company colour scheme. Cards can be horizontal or vertical format.
We are looking for a two sided business card - on the front we will see the personal details of the employee (name, position, email and phone number), and then on the back, we will see the business details (name and logo, address, phone number, website, email, company tagline: "Accelerating technology disruption in the automotive market")
We want the design to be clean and simple, but also fun, modern, and capturing of a young startup vibe.

```html
<!DOCTYPE html>
<html lang="en">
<head>
<meta charset="utf-8">
<title>Korimo Business Cards</title>
<link rel="stylesheet" href="https://fonts.googleapis.com/css2?family=Comfortaa:wght@400;600;700&family=Montserrat:wght@400;600;700&display=swap">
<style>
  :root {
    --backdrop: #5a4cd0;
    --brand-violet: #4330c6;
    --brand-ink: #3b2bbf;
    --accent-orchid: #c052d8;
    --paper: #f7f6f8;
    --paper-shade: #ece9f1;
    --white: #ffffff;
  }
  * { box-sizing: border-box; margin: 0; padding: 0; }
  html, body {
    width: 1200px; height: 900px; overflow: hidden;
    background: var(--backdrop);
  }
  .sheet {
    position: relative; width: 1200px; height: 900px;
    display: flex; align-items: center; justify-content: center; gap: 60px;
  }
  .card {
    position: relative; width: 510px; height: 292px;
    border-radius: 4px; overflow: hidden;
    box-shadow: 0 30px 50px rgba(30, 18, 110, 0.35);
  }
  /* Front: personal details */
  .card--front { background: var(--brand-violet); color: var(--white); }
  .card--front .wordmark {
    position: absolute; left: 40px; bottom: 110px;
    display: flex; align-items: center; gap: 10px;
    font-family: "Comfortaa", sans-serif; font-weight: 700; font-size: 30px;
    color: var(--white);
  }
  .contact {
    position: absolute; right: 44px; bottom: 40px; width: 210px;
    font-family: "Montserrat", sans-serif;
  }
  .contact__name {
    font-weight: 700; font-size: 15px; letter-spacing: 0.16em;
  }
  .contact__role {
    font-size: 11px; letter-spacing: 0.16em; color: var(--accent-orchid);
    margin-top: 3px; margin-bottom: 12px;
  }
  .contact__line {
    font-family: "Comfortaa", sans-serif;
    font-size: 12px; letter-spacing: 0.06em; line-height: 1.7;
  }
  /* Back: company details */
  .card--back { background: var(--paper); color: var(--brand-ink); }
  .card--back .decor {
    position: absolute; right: 0; top: 0; width: 55%; height: 100%;
    background: radial-gradient(circle at 60% 45%, var(--paper-shade) 0%, rgba(236,233,241,0.5) 45%, rgba(247,246,248,0) 75%);
  }
  .brand {
    position: absolute; left: 36px; top: 34px;
    display: flex; align-items: center; gap: 14px;
  }
  .brand__dot {
    width: 44px; height: 44px; border-radius: 50%; background: var(--brand-violet);
  }
  .brand__name {
    font-family: "Comfortaa", sans-serif; font-weight: 700; font-size: 46px;
    color: var(--brand-ink);
  }
  .details {
    position: absolute; left: 40px; top: 124px;
    font-family: "Comfortaa", sans-serif; font-size: 13px;
    line-height: 1.75; color: var(--accent-orchid); letter-spacing: 0.02em;
  }
  .tagline {
    position: absolute; left: 40px; bottom: 24px;
    font-family: "Comfortaa", sans-serif; font-weight: 600; font-size: 10.5px;
    color: var(--brand-ink);
  }
</style>
</head>
<body>
<main class="sheet">
  <section class="card card--front" aria-label="Business card front">
    <div class="wordmark">korimo</div>
    <div class="contact">
      <p class="contact__name">YOUR NAME</p>
      <p class="contact__role">YOUR POSITION</p>
      <p class="contact__line">+00-0000-0000-000</p>
      <p class="contact__line">info@korimo.com</p>
    </div>
  </section>

  <section class="card card--back" aria-label="Business card back">
    <div class="decor" role="img" aria-label="Faint brand pattern in soft grey-lilac"></div>
    <div class="brand">
      <span class="brand__dot"></span>
      <span class="brand__name">korimo</span>
    </div>
    <div class="details">
      <p>1234 your location here, State, Country</p>
      <p>+00-0000-0000-000</p>
      <p>www.korimo.com</p>
      <p>info@korimo.com</p>
    </div>
    <p class="tagline">Accelerating technology disruption in the automotive market</p>
  </section>
</main>
</body>
</html>
```